Tallowreed Consulting Schedule Of Rates

We need a brochure / proposal for our new company. Our company is a start up based in Australia who provides engineering and sales support to other renewable energy companies. Our brochure is a pitch-deck / sales item that catalogues our key services. We are engineering consultants.

Our website is www.tallowreedpartners.com.au. Please review the website to get a feel of colour schemes etc.

We are looking for a strong, trustworthy feel, but the brochure also needs to be sales driven and to the point.

The second page that contains the $30 price point needs to be loud and clear.

The use of relevant icons throughout the document will be viewed favorably.

Please format the tables to look attractive.

The document will need to be in an editable format so content can be edited by us at a later date.

Please feel free to use the pics within the attached word document. The winning design will be provided with updated, clearer images upon request.

Thank you

Target Market(s)

Businesses that either sell or install solar PV and other renewable energy systems in Australia. Most of target market are likely to be electrical contractors.

Industry/Entity Type

Engineering

Colors
0255a3
0492cd
ffffff

Requirements
Must have
• Icons, graphics presentation, Clean and Clear, Business oriented. Sharp sales feel
Nice to have
• solar picture backgrounds maybe
Should not have
• cartoons, over sales driven,

```html
<!DOCTYPE html>
<html lang="en">
<head>
<meta charset="utf-8">
<title>Tallowreed Consulting – Schedule Of Rates</title>
<link href="https://fonts.googleapis.com/css2?family=Exo+2:wght@400;600;700;800&display=swap" rel="stylesheet">
<style>
  :root{
    --stage:#e6e7e8;
    --paper:#ffffff;
    --charcoal:#3c3c3e;
    --ink:#111111;
    --steel:#86878a;
    --muted:#b9babc;
    --sky-light:#cfd8e6;
    --solar-deep:#0255a3;
    --solar-mid:#0492cd;
    --sun:#e9e36a;
    --text:#1d1d1f;
  }
  *{margin:0;padding:0;box-sizing:border-box}
  html,body{width:1200px;height:800px;overflow:hidden;background:var(--stage)}
  body{font-family:"Exo 2",sans-serif;color:var(--text);position:relative}
  .page{position:absolute;top:46px;width:500px;height:707px;background:var(--paper);overflow:hidden;box-shadow:0 2px 10px rgba(0,0,0,.15)}
  .page--rates{left:100px}
  .page--cover{left:600px}
  .page svg.shapes{position:absolute;inset:0;width:500px;height:707px}
  .abs{position:absolute}

  /* rates page */
  .services{left:40px;top:48px}
  .services__title{font-size:21px;font-weight:700;letter-spacing:.3px}
  .services__lead{font-size:15px;margin-top:6px}
  .services__list{list-style:none;margin-top:4px;font-size:15px;line-height:1.35}
  .services__list li::before{content:"";display:inline-block;width:6px;height:6px;border-radius:50%;background:var(--text);margin-right:9px;vertical-align:middle}

  .offer{left:48px;top:232px;color:var(--paper);text-transform:uppercase;line-height:1}
  .offer__limit{font-size:21px;font-weight:600;letter-spacing:.5px}
  .offer__price{font-size:112px;font-weight:800;letter-spacing:-3px;margin-top:-4px}
  .offer__note{font-size:16px;font-weight:600;margin-left:48px;margin-top:-6px}
  .offer__product{font-size:27px;font-weight:700;margin-left:26px;margin-top:3px}

  .tiers{left:262px;top:222px;width:210px;color:var(--paper);list-style:none}
  .tier{padding:8px 0 8px 14px;border-left:1px solid var(--steel);border-bottom:1px solid var(--steel);font-size:13px;line-height:1.25}
  .tier:last-child{border-bottom:none}
  .tier__range{font-weight:600}
  .tier__price{font-weight:700;font-size:14px}

  .brand{font-size:27px;font-weight:700;color:var(--ink);display:flex;align-items:center;gap:8px;letter-spacing:-.3px}
  .brand__mark{width:12px;height:12px;background:var(--ink)}
  .brand--rates{right:30px;top:608px}
  .contact{font-size:9.5px;line-height:1.5}
  .contact--rates{left:40px;top:650px}

  /* cover page */
  .cover-title{left:26px;top:282px;color:var(--paper);font-weight:400}
  .cover-title__main{font-size:23px;line-height:1.2}
  .cover-title__sub{font-size:12.5px;color:var(--muted);margin-top:8px}
  .contact--cover{left:26px;top:600px;color:var(--paper);font-size:8.5px}
  .brand--cover{right:24px;top:568px;font-size:26px}
</style>
</head>
<body>

<section class="page page--rates" aria-label="Panel layout rates page">
  <svg class="shapes" viewBox="0 0 500 707">
    <defs>
      <linearGradient id="solarFieldA" x1="0" y1="0" x2="1" y2="1">
        <stop offset="0" stop-color="#c9c77a"/>
        <stop offset=".25" stop-color="#4f63b8"/>
        <stop offset="1" stop-color="#2c3f9a"/>
      </linearGradient>
    </defs>
    <polygon points="0,390 500,320 500,540 0,612" fill="url(#solarFieldA)" role="img" aria-label="Photo of a solar farm with rows of panels"/>
    <polygon points="0,200 500,140 500,385 0,455" fill="var(--charcoal)"/>
    <polygon points="0,193 500,131 500,140 0,200" fill="var(--ink)"/>
    <polygon points="0,612 500,540 500,546 0,618" fill="var(--ink)"/>
  </svg>

  <div class="abs services">
    <h2 class="services__title">Services – Professional Panel Layout</h2>
    <p class="services__lead">We can layout the panels for a small fee</p>
    <ul class="services__list">
      <li>Clear &amp; Concise</li>
      <li>Ranging from 5kW – 300kW</li>
    </ul>
  </div>

  <div class="abs offer">
    <p class="offer__limit">Less then 30kW</p>
    <p class="offer__price">$30</p>
    <p class="offer__note">Ex. GST Skyplan</p>
    <p class="offer__product">Panel Layout</p>
  </div>

  <ul class="abs tiers">
    <li class="tier"><span class="tier__range">30KW – 100KW</span><br><span class="tier__price">$80 Ex. Gst Skyplan</span><br>Panel Layout</li>
    <li class="tier"><span class="tier__range">101KW – 300KW</span><br><span class="tier__price">$150 Ex. Gst Skyplan</span><br>Panel Layout</li>
    <li class="tier"><span class="tier__range">300KW + $360 Ex. Gst</span><br><span class="tier__price">3D Drawings including</span><br>shading analysis</li>
  </ul>

  <div class="abs brand brand--rates"><span class="brand__mark"></span>Tallowreed Consulting</div>

  <div class="abs contact contact--rates">
    <p>P: 03 9100 4821 | M: 0412 660 318</p>
    <p>E: sales@tallowreedpartners.com.au</p>
    <p>W: www.tallowreedpartners.com.au</p>
  </div>
</section>

<section class="page page--cover" aria-label="Cover page">
  <svg class="shapes" viewBox="0 0 500 707">
    <defs>
      <linearGradient id="solarFieldB" x1="0" y1="0" x2="0.6" y2="1">
        <stop offset="0" stop-color="var(--sun)"/>
        <stop offset=".12" stop-color="#9fb6d6"/>
        <stop offset=".4" stop-color="var(--solar-mid)"/>
        <stop offset="1" stop-color="var(--solar-deep)"/>
      </linearGradient>
    </defs>
    <rect x="0" y="0" width="500" height="540" fill="url(#solarFieldB)" role="img" aria-label="Photo of solar panel rows lit by the sun"/>
    <polygon points="0,300 290,238 290,470 0,500" fill="var(--ink)"/>
    <polygon points="0,500 270,472 270,707 0,707" fill="var(--steel)"/>
    <polygon points="270,472 290,238 300,238 284,707 270,707" fill="var(--ink)"/>
    <polygon points="300,238 310,232 298,460 290,470" fill="var(--steel)"/>
    <polygon points="296,470 500,428 500,707 284,707" fill="var(--paper)"/>
  </svg>

  <div class="abs cover-title">
    <h1 class="cover-title__main">Design &amp; Support Services<br>Schedule Of Rates</h1>
    <p class="cover-title__sub">Grid and Off Grid 5kW – 10MW</p>
  </div>

  <div class="abs contact contact--cover">
    <p>P: 03 9100 4821 | M: 0412 660 318</p>
    <p>E: sales@tallowreedpartners.com.au</p>
    <p>W: www.tallowreedpartners.com.au</p>
  </div>

  <div class="abs brand brand--cover"><span class="brand__mark"></span>Tallowreed<br>Consulting</div>
</section>

</body>
</html>
```